company anniversary card

Create a single-sided postcard
Background: Yellow
Message: “88 Jahre FALKAAAAN! Danke für die tOOOOle Zusammenarbeit.”
The three different logos can be used, as well as the old photo.
I’m open to further suggestions — you can find more ideas at www.falkaaaan.ch.

```html
<!DOCTYPE html>
<html lang="de">
<head>
<meta charset="utf-8">
<title>88 Jahre FALKAAAAN – Postkarte</title>
<link rel="stylesheet" href="https://fonts.googleapis.com/css2?family=Montserrat:wght@500;700;800;900&family=Permanent+Marker&display=swap">
<style>
  :root {
    --yellow-light: #f7e871;
    --yellow: #f0d834;
    --yellow-deep: #dcbd22;
    --mustard: #b59a2a;
    --ink: #141414;
    --white: #ffffff;
  }
  * { margin: 0; padding: 0; box-sizing: border-box; }
  html, body { width: 887px; height: 1200px; overflow: hidden; }
  body { background: var(--yellow); font-family: "Montserrat", sans-serif; color: var(--ink); }

  .postcard {
    position: relative;
    width: 887px;
    height: 1200px;
    overflow: hidden;
    background: radial-gradient(ellipse at 50% 40%, var(--yellow-light) 0%, var(--yellow) 55%, var(--yellow-deep) 100%);
  }

  .brand { position: absolute; top: 52px; left: 0; width: 100%; text-align: center; }
  .brand__name { font-weight: 900; font-size: 66px; letter-spacing: 1px; line-height: 1; }
  .brand__trade { margin-top: 10px; font-weight: 500; font-size: 19px; letter-spacing: 5px; }

  .anniversary { position: absolute; top: 168px; left: 0; width: 100%; height: 300px; }
  .anniversary__number {
    position: absolute; left: 0; width: 100%; top: -30px;
    text-align: center; font-weight: 800; font-size: 380px; line-height: 1; letter-spacing: -18px;
  }
  .anniversary__label {
    position: absolute; top: 212px; left: 300px;
    padding: 0 10px; background: var(--yellow-light);
    font-weight: 800; font-size: 46px; letter-spacing: 1px; line-height: 1.05;
  }

  .ribbon { position: absolute; top: 448px; left: 200px; width: 487px; height: 86px; }
  .ribbon__text {
    position: absolute; inset: 0; display: flex; align-items: center; justify-content: center;
    color: var(--white); font-weight: 900; font-size: 48px; letter-spacing: 1px;
  }

  .message { position: absolute; top: 548px; left: 0; width: 100%; text-align: center; font-family: "Permanent Marker", cursive; line-height: 1.05; }
  .message__lead { font-size: 74px; }
  .message__word { font-size: 60px; letter-spacing: 2px; }

  .old-photo {
    position: absolute; top: 740px; left: 0; width: 100%; height: 400px;
    background: linear-gradient(to bottom, rgba(240,216,52,0) 0%, #cdb44a 30%, #a99240 65%, #8e7a36 100%);
  }

  .footer-band {
    position: absolute; bottom: 0; left: 0; width: 100%; height: 72px;
    background: var(--mustard);
    display: flex; align-items: center; justify-content: center; gap: 70px;
    color: var(--white); font-weight: 800;
  }
  .footer-band__jubilee { font-size: 30px; letter-spacing: 1px; }
  .footer-band__mark { display: flex; align-items: center; gap: 10px; font-size: 30px; }
  .footer-band__dot { width: 24px; height: 24px; border-radius: 50%; background: var(--white); }
</style>
</head>
<body>
  <main class="postcard">
    <header class="brand">
      <div class="brand__name">FALKAAAAN</div>
      <div class="brand__trade">HAUSTECHNIK + BAUSPENGLEREI</div>
    </header>

    <section class="anniversary">
      <div class="anniversary__number">88</div>
      <div class="anniversary__label">JAHRE</div>
    </section>

    <div class="ribbon">
      <svg width="487" height="86" viewBox="0 0 487 86" aria-hidden="true">
        <polygon points="0,14 40,14 40,78 0,78 16,46" fill="#141414"/>
        <polygon points="487,14 447,14 447,78 487,78 471,46" fill="#141414"/>
        <polygon points="40,78 58,86 58,70" fill="#000"/>
        <polygon points="447,78 429,86 429,70" fill="#000"/>
        <rect x="40" y="6" width="407" height="72" rx="2" fill="#141414"/>
      </svg>
      <div class="ribbon__text">FALKAAAAN!</div>
    </div>

    <section class="message">
      <div class="message__lead">Danke für die</div>
      <div class="message__word">TOOOOLE</div>
      <div class="message__word">ZUSAMMENARBEIT</div>
    </section>

    <div class="old-photo" role="img" aria-label="Historisches Foto: Firmenfahrzeuge vor Kapellbrücke und Wasserturm am Seeufer"></div>

    <footer class="footer-band">
      <div class="footer-band__jubilee">88 JAAAAHR</div>
      <div class="footer-band__mark"><span class="footer-band__dot"></span>FALKAAAAN</div>
    </footer>
  </main>
</body>
</html>
```